2026 Company Line Card

We would like to redesign our current company line card. We send this printed flyer to prospective customers to introduce our company, the brands we represent, and our competitive advantages. Our website is www.pipelornsupply.com, and our phone number is (800) 341-2867. We're a specialty supplier for plumbing material, specifically water and life safety products. Our customers are mostly male, blue-collar contractors, ages 40-60. I have included a pdf of our current flyer and our high-resolution transparent logo. We would also like to highlight certain key points, which include:
Genuine OEM Parts
Technical Assistance from Repair Experts
Repair Information
1-2 day Delivery for the United States
Friendly & Knowledgeable Customer Service
The Largest Parts Inventory In The Nation
Testing Equipment
Full Service Gauge Calibration and Repair

```html
<!DOCTYPE html>
<html lang="en">
<head>
<meta charset="utf-8">
<title>Pipelorn Supply Company – Line Card</title>
<link href="https://fonts.googleapis.com/css2?family=Catamaran:wght@400;600;700;800&display=swap" rel="stylesheet">
<style>
:root{
  --navy:#0a4a9a;
  --blue:#1a5ba8;
  --red:#e63a46;
  --white:#ffffff;
  --ink:#1d1d1d;
}
*{margin:0;padding:0;box-sizing:border-box}
html,body{width:848px;height:1200px;overflow:hidden;background:var(--white)}
body{font-family:"Catamaran",sans-serif;position:relative;color:var(--ink)}
.hero{position:absolute;left:0;top:0;width:848px;height:370px;
  background:linear-gradient(180deg,#3f5528 0%,#56703a 45%,#6b7f4a 70%,#8a9770 100%);}
.hero-shade{position:absolute;left:0;top:0;width:848px;height:370px;
  background:linear-gradient(90deg,rgba(20,30,15,.55) 0%,rgba(20,30,15,.15) 50%,rgba(20,30,15,0) 100%)}
.brand{position:absolute;left:44px;top:18px;display:flex;align-items:center;gap:10px;color:var(--white)}
.brand-mark{width:14px;height:14px;background:var(--red)}
.brand-name{font-size:30px;font-weight:600;line-height:1}
.brand-sub{font-size:14px;font-weight:400;line-height:1.2;margin-top:2px}
.phone-tab{position:absolute;right:0;top:0;width:298px;height:35px;background:var(--red);
  border-bottom-left-radius:26px;display:flex;align-items:center;justify-content:center;gap:8px;
  color:var(--white);font-size:28px;font-weight:700}
.phone-tab svg{width:26px;height:26px}
.tagline{position:absolute;left:41px;top:112px;color:var(--white);font-size:17px;font-weight:800}
.services-head{position:absolute;left:41px;top:141px;color:var(--white);font-size:30px;font-weight:700;line-height:33px}
.waves{position:absolute;left:0;top:290px;width:848px;height:100px}
.left-panel{position:absolute;left:0;top:355px;width:424px;height:330px;
  background:linear-gradient(180deg,#2f6fba 0%,#6c9ad2 35%,#dbe6f4 75%,#ffffff 100%)}
.intro-title{position:absolute;left:42px;top:362px;color:var(--white);font-size:26px;font-weight:800;line-height:30px}
.intro-text{position:absolute;left:42px;top:465px;width:339px;font-size:14.5px;line-height:25px;text-align:justify;color:#1a1a1a}
.photo-grid{position:absolute;left:42px;top:673px;width:338px;height:248px;border-radius:24px;overflow:hidden;
  display:grid;grid-template-columns:165px 173px;grid-template-rows:131px 117px;gap:1px;background:#fff}
.photo-grid div{background:linear-gradient(135deg,#b08a4e,#6d6a66)}
.photo-grid div:nth-child(2){background:linear-gradient(135deg,#8a7a5a,#3a7ed6)}
.photo-grid div:nth-child(4){background:linear-gradient(135deg,#e6e6e6,#8a8a8a)}
.features{position:absolute;left:460px;top:367px;width:345px;list-style:none}
.feature{position:relative;height:57px;margin-bottom:14px}
.feature-bar{position:absolute;left:50px;top:0;right:0;height:57px;background:var(--navy);border-radius:0 29px 29px 0;
  display:flex;align-items:center;padding-left:33px;color:var(--white);font-size:18px;font-weight:700;line-height:23px;z-index:1}
.feature-hex{position:absolute;left:0;top:0;width:66px;height:57px;z-index:2}
.brands{position:absolute;left:42px;top:954px;width:764px;display:grid;grid-template-columns:repeat(6,118px);
  grid-auto-rows:67px;column-gap:11px;row-gap:19px}
.brand-tile{background:var(--white);border-radius:10px;box-shadow:0 2px 8px rgba(0,0,0,.12);
  display:flex;align-items:center;justify-content:center;font-size:15px;font-weight:800;color:var(--navy)}
.footer{position:absolute;left:0;top:1138px;width:848px;height:62px}
.footer-red{position:absolute;left:0;top:20px;width:848px;height:42px;background:var(--red)}
.footer-blue{position:absolute;left:0;top:0;width:340px;height:62px;background:var(--navy);
  clip-path:polygon(0 0,275px 0,340px 62px,0 62px)}
.footer-cta{position:absolute;left:42px;top:8px;color:var(--white);font-size:17.5px;font-weight:800;line-height:24px}
.footer-contact{position:absolute;left:350px;top:20px;height:42px;display:flex;align-items:center;gap:8px;
  color:var(--white);font-size:19px;font-weight:700}
.footer-contact .ic{width:28px;height:28px;border-radius:50%;background:var(--white);display:flex;align-items:center;justify-content:center}
.footer-contact .sep{margin:0 20px;font-weight:400}
</style>
</head>
<body>
<section class="hero" role="img" aria-label="Photo of a blue backflow prevention assembly on a grassy field discharging water"></section>
<div class="hero-shade"></div>

<div class="brand">
  <span class="brand-mark"></span>
  <div><div class="brand-name">Pipelorn Supply</div><div class="brand-sub">Company</div></div>
</div>

<div class="phone-tab">
  <svg viewBox="0 0 24 24"><circle cx="12" cy="12" r="12" fill="#fff"/><path d="M8 6l2.5 2.6-1.3 1.6c.8 1.7 2 2.9 3.6 3.7l1.6-1.3L17 15l-1.4 2.5c-4.8-.6-8.5-4.3-9.1-9.1z" fill="#e63a46"/></svg>
  (800) 341-2867
</div>

<div class="tagline">THE NATION'S LEADING SOURCE FOR:</div>
<div class="services-head">Genuine OEM Parts<br>Repair Information<br>Technical Assistance</div>

<svg class="waves" viewBox="0 0 848 100" preserveAspectRatio="none">
  <path d="M0 66 C90 12 200 0 300 10 C360 16 400 34 424 66 L424 100 L0 100Z" fill="#2a68b4"/>
  <path d="M424 66 C480 30 560 10 640 14 C720 18 790 40 848 66 L848 100 L424 100Z" fill="#fff"/>
</svg>
<div class="left-panel"></div>

<h1 class="intro-title">YOUR TRUSTED SOURCE<br>FOR WATER &amp; LIFE SAFETY<br>PRODUCTS</h1>
<p class="intro-text">For over 30 years, contractors nationwide have relied on us for genuine OEM backflow parts, fast shipping, and expert technical support. We stock the largest backflow parts inventory in the country, ensuring you get the right part, right when you need it. Whether you're repairing assemblies, testing equipment, or maintaining critical water safety systems, our team is here to help you keep your jobs moving.</p>

<div class="photo-grid">
  <div role="img" aria-label="Hands holding a brass check valve seat"></div>
  <div role="img" aria-label="Technician removing a spring check from a blue valve body"></div>
  <div role="img" aria-label="Hand fitting a rubber seal into a bronze valve flange"></div>
  <div role="img" aria-label="Wrench loosening a grey valve cover"></div>
</div>

<ul class="features">
  <li class="feature"><svg class="feature-hex" viewBox="0 0 66 57"><path d="M14 0H52L66 28.5 52 57H14L0 28.5Z" fill="#e63a46"/><circle cx="33" cy="28.5" r="10" fill="none" stroke="#fff" stroke-width="3"/><circle cx="33" cy="28.5" r="3" fill="#fff"/></svg><div class="feature-bar">Genuine OEM Parts</div></li>
  <li class="feature"><svg class="feature-hex" viewBox="0 0 66 57"><path d="M14 0H52L66 28.5 52 57H14L0 28.5Z" fill="#e63a46"/><circle cx="33" cy="21" r="7" fill="none" stroke="#fff" stroke-width="2.5"/><path d="M21 44c0-8 5-12 12-12s12 4 12 12" fill="none" stroke="#fff" stroke-width="2.5"/></svg><div class="feature-bar">Technical Assistance from<br>Repair Experts</div></li>
  <li class="feature"><svg class="feature-hex" viewBox="0 0 66 57"><path d="M14 0H52L66 28.5 52 57H14L0 28.5Z" fill="#e63a46"/><rect x="19" y="16" width="28" height="19" rx="2" fill="none" stroke="#fff" stroke-width="2.5"/><path d="M33 35v6M26 42h14" stroke="#fff" stroke-width="2.5"/></svg><div class="feature-bar">Repair Information</div></li>
  <li class="feature"><svg class="feature-hex" viewBox="0 0 66 57"><path d="M14 0H52L66 28.5 52 57H14L0 28.5Z" fill="#e63a46"/><path d="M18 20h19v15H18zM37 24h6l4 5v6H37z" fill="#fff"/><circle cx="24" cy="37" r="3" fill="#e63a46" stroke="#fff" stroke-width="2"/><circle cx="42" cy="37" r="3" fill="#e63a46" stroke="#fff" stroke-width="2"/></svg><div class="feature-bar">1-2 day Delivery for the<br>United States</div></li>
  <li class="feature"><svg class="feature-hex" viewBox="0 0 66 57"><path d="M14 0H52L66 28.5 52 57H14L0 28.5Z" fill="#e63a46"/><path d="M22 18h22a3 3 0 013 3v11a3 3 0 01-3 3H30l-6 5v-5h-2a3 3 0 01-3-3V21a3 3 0 013-3z" fill="none" stroke="#fff" stroke-width="2.5"/><circle cx="27" cy="26.5" r="1.8" fill="#fff"/><circle cx="33" cy="26.5" r="1.8" fill="#fff"/><circle cx="39" cy="26.5" r="1.8" fill="#fff"/></svg><div class="feature-bar">Friendly &amp; Knowledgeable<br>Customer Service</div></li>
  <li class="feature"><svg class="feature-hex" viewBox="0 0 66 57"><path d="M14 0H52L66 28.5 52 57H14L0 28.5Z" fill="#e63a46"/><path d="M19 31h28v11H19z" fill="#fff"/><circle cx="26" cy="21" r="5" fill="none" stroke="#fff" stroke-width="2.5"/><path d="M38 14l6 12" stroke="#fff" stroke-width="3"/></svg><div class="feature-bar">The Largest Parts Inventory<br>In The Nation</div></li>
  <li class="feature"><svg class="feature-hex" viewBox="0 0 66 57"><path d="M14 0H52L66 28.5 52 57H14L0 28.5Z" fill="#e63a46"/><rect x="20" y="17" width="26" height="24" fill="none" stroke="#fff" stroke-width="2.5"/><path d="M23 35l6-6 5 4 8-9" fill="none" stroke="#fff" stroke-width="2.5"/></svg><div class="feature-bar">Testing Equipment</div></li>
  <li class="feature"><svg class="feature-hex" viewBox="0 0 66 57"><path d="M14 0H52L66 28.5 52 57H14L0 28.5Z" fill="#e63a46"/><circle cx="33" cy="28.5" r="12" fill="none" stroke="#fff" stroke-width="2.5" stroke-dasharray="14 5"/><circle cx="33" cy="25" r="4" fill="#fff"/><path d="M26 36c2-4 12-4 14 0" fill="none" stroke="#fff" stroke-width="2.5"/></svg><div class="feature-bar">Full Service Gauge Calibration<br>and Repair</div></li>
</ul>

<div class="brands">
  <div class="brand-tile">Halvorsen</div>
  <div class="brand-tile">Brennick</div>
  <div class="brand-tile">Corvale</div>
  <div class="brand-tile">Tamsford Valves</div>
  <div class="brand-tile">Rutherby</div>
  <div class="brand-tile">Ostrand</div>
  <div class="brand-tile">Delmore</div>
  <div class="brand-tile">Kestline Gauge</div>
  <div class="brand-tile">Varnell</div>
  <div class="brand-tile">Shieldwell</div>
  <div class="brand-tile">Thermcase</div>
  <div class="brand-tile">Quillon</div>
</div>

<footer class="footer">
  <div class="footer-red"></div>
  <div class="footer-blue"></div>
  <div class="footer-cta">CONTACT US FOR MORE<br>INFORMATION</div>
  <div class="footer-contact">
    <span class="ic"><svg width="20" height="20" viewBox="0 0 24 24" fill="none" stroke="#e63a46" stroke-width="2"><circle cx="12" cy="12" r="9"/><path d="M3 12h18M12 3c3 3 3 15 0 18M12 3c-3 3-3 15 0 18"/></svg></span>
    www.pipelornsupply.com
    <span class="sep">|</span>
    <span class="ic"><svg width="20" height="20" viewBox="0 0 24 24"><path d="M6 4l3 3-1.5 2c1 2 2.5 3.5 4.5 4.5l2-1.5 3 3-1.7 3C9.5 17.3 6.7 14.5 4.4 9.7z" fill="#e63a46"/></svg></span>
    800-341-2867
  </div>
</footer>
</body>
</html>
```